Residential technology services business card

Looking for a simple, catchy, slightly fun business card design.

We are a residential technology service provider (computer repair, tablet repair, training, etc). We are a fun, upbeat, yet professional company that is very skilled at our job.

I will upload our logo in a sec, thinking that it should be the only thing on the front side of the card, with maybe a punch line as well... maybe not. Maybe the punchline can find a place on the back. You be the judge.

Backside should be minimal in terms of information. I need two variations: one that will only have our website and phone and one that will also include a persons name (and position), personal e-mail and personal phone.

Well, you're the designer, figure out the best way to place all above mentioned items.

Colors are white, black, green (as in logo), plus whatever else you think needs adding (if any).

It must be clear to people what we do (provide computer services, tablet services)... without using generic pictures of computers and tablets, unless it 's something original.

We want something original! But do note that the card will be printed on standard size business card paper, so no funky shapes please.

Thanks!!!

Residential

Requirements
Must have
• Logo, website, phone.
2nd variation also must include space for persons name, personal phone and email.

```html
<!DOCTYPE html>
<html lang="en">
<head>
<meta charset="utf-8">
<title>ByteNest Business Card – Front and Back</title>
<link rel="stylesheet" href="https://fonts.googleapis.com/css2?family=Didact+Gothic&family=Questrial&family=Indie+Flower&display=swap">
<style>
  :root {
    --paper: #ffffff;
    --ink: #111111;
    --brand-green: #7ee01f;
    --green-bright: #9cf04a;
    --green-soft: #b4f56e;
    --green-pale: #d2fba8;
    --card-edge: #8a8a8a;
  }
  * { box-sizing: border-box; margin: 0; padding: 0; }
  html, body {
    width: 1200px;
    height: 375px;
    overflow: hidden;
    background: var(--paper);
  }
  .sheet {
    position: relative;
    width: 1200px;
    height: 375px;
    background: var(--paper);
  }
  .card {
    position: absolute;
    top: 27px;
    width: 548px;
    height: 314px;
    border: 1px solid var(--card-edge);
    background: var(--paper);
    overflow: hidden;
  }
  .card--front { left: 23px; }
  .card--back { left: 613px; }

  .brand {
    position: absolute;
    display: flex;
    align-items: center;
    gap: 10px;
    font-family: "Questrial", sans-serif;
    color: var(--ink);
    white-space: nowrap;
  }
  .brand__dot {
    display: block;
    border-radius: 50%;
    background: var(--brand-green);
  }
  .card--front .brand {
    left: 0;
    right: 0;
    top: 96px;
    justify-content: center;
    font-size: 50px;
  }
  .card--front .brand__dot { width: 26px; height: 26px; }

  .tagline {
    position: absolute;
    left: 0;
    right: 0;
    top: 241px;
    text-align: center;
    font-family: "Didact Gothic", sans-serif;
    font-size: 21px;
    color: var(--brand-green);
    white-space: nowrap;
  }
  .tagline__at { font-size: 28px; vertical-align: -2px; }

  .card--back .brand {
    left: 28px;
    top: 50px;
    font-size: 26px;
    gap: 6px;
  }
  .card--back .brand__dot { width: 14px; height: 14px; }

  .contact {
    position: absolute;
    left: 162px;
    width: 370px;
    text-align: center;
    white-space: nowrap;
  }
  .contact__web {
    top: 38px;
    font-family: "Didact Gothic", sans-serif;
    font-size: 36px;
    color: var(--brand-green);
  }
  .contact__phone {
    top: 94px;
    font-family: "Didact Gothic", sans-serif;
    font-size: 38px;
    letter-spacing: 3px;
    color: var(--ink);
  }
  .slogan {
    position: absolute;
    left: 162px;
    width: 370px;
    top: 163px;
    text-align: center;
    font-family: "Indie Flower", cursive;
    font-size: 24px;
    color: var(--ink);
    white-space: nowrap;
  }
  .tile-band {
    position: absolute;
    left: 0;
    bottom: 0;
    width: 548px;
    height: 78px;
    background: linear-gradient(90deg, var(--green-soft) 0%, var(--green-bright) 30%, var(--green-pale) 55%, var(--green-bright) 78%, var(--green-soft) 100%);
  }
</style>
</head>
<body>
<main class="sheet">
  <section class="card card--front" aria-label="Card front">
    <div class="brand"><span class="brand__dot"></span><span class="brand__name">ByteNest</span></div>
    <p class="tagline">computer services <span class="tagline__at">@</span> your home</p>
  </section>

  <section class="card card--back" aria-label="Card back">
    <div class="brand"><span class="brand__dot"></span><span class="brand__name">ByteNest</span></div>
    <p class="contact contact__web">www.bytenest.com</p>
    <p class="contact contact__phone">1800 555 010</p>
    <p class="slogan">your technical service provider</p>
    <div class="tile-band" role="img" aria-label="Decorative band of scattered translucent green tiles"></div>
  </section>
</main>
</body>
</html>
```